Tarvon Letterhead

Looking for a design template for our company’s official letterheads & business cards.It has to be mainly white and include our company logo, website, social media handle, address, phone number. Visit our website to have an idea of our brand identity and colours. Please use the same font that we are using in our website.
Target Market(s)
Lubricants & Greases, Industrial markets, Automotive
Font styles to use
Other font styles liked:
- Saira Extra-Condensed
Colors
ffffff
000000
fbee3f
Requirements
Must have
- It must be consistent with our brand identity. It must use the same exact yellow (Pantone color: 102C) and black (Pantone color: K100) as our brand colors.
- Must also use our font attached (Saira.zip). It's called Saira Extra-Condensed.
- We intend to use the TARVON logo and not the small mini-TV logo.
- On the design we must include ALL of the following:
- E-mail: info@tarvonfluids.example
- @TarvonFluids
- www.tarvonfluids.example
- Address: P.O. Boc 4827, Qurain 73504, Kuwait
- Phone: (+965) 24718593
- Kuwait Morel Oils logo (attached). The logo attached is in Blue/Red but you can select one solid color for all of it such as BLACK or YELLOW depending on what background color you'll select.
Nice to have
- Like it to be as professional and as modern as possible. It has look clean, slick and classy.
Should not have
- Too many different colors.

```html
<!DOCTYPE html>
<html lang="en">
<head>
<meta charset="utf-8">
<title>Tarvon Letterhead</title>
<link rel="stylesheet" href="https://fonts.googleapis.com/css2?family=Montserrat:wght@400;500&family=Saira+Extra+Condensed:wght@500;700;800&display=swap">
<style>
  :root {
    --brand-yellow: #fbee3f;
    --brand-black: #000000;
    --ink: #1a1a1a;
    --paper: #ffffff;
    --backdrop: #e6e8eb;
    --footer-text: #d9d9d9;
    --signature-tone: #dfe4f3;
  }
  * { margin: 0; padding: 0; box-sizing: border-box; }
  html, body { width: 1200px; height: 900px; overflow: hidden; }
  body { background: var(--backdrop); font-family: "Montserrat", Arial, sans-serif; }

  .letterhead {
    position: absolute; left: 296px; top: 20px;
    width: 608px; height: 860px;
    background: var(--paper);
    box-shadow: 0 4px 18px rgba(0,0,0,0.18);
    overflow: hidden;
  }

  .header-band {
    position: absolute; left: 0; top: 0; width: 100%; height: 62px;
    background: var(--brand-black);
  }
  .brand-name {
    position: absolute; left: 150px; top: 4px;
    font-family: "Saira Extra Condensed", "Arial Narrow", sans-serif;
    font-weight: 800; font-size: 54px; line-height: 54px; letter-spacing: 2px;
    color: var(--brand-yellow);
  }
  .tagline-ribbon { position: absolute; right: 0; top: 62px; width: 250px; height: 24px; }
  .tagline-text {
    position: absolute; right: 12px; top: 66px;
    font-family: "Saira Extra Condensed", "Arial Narrow", sans-serif;
    font-weight: 700; font-size: 13px; letter-spacing: 0.6px; line-height: 16px;
    color: var(--brand-black); white-space: nowrap;
  }

  .letter-body {
    position: absolute; left: 70px; top: 150px; width: 468px;
    font-size: 10.5px; line-height: 17px; color: var(--ink); text-align: justify;
  }
  .letter-body p { margin-bottom: 14px; }

  .sign-off { position: absolute; left: 70px; top: 405px; }
  .signature-area { width: 130px; height: 34px; background: var(--signature-tone); border-radius: 3px; }
  .signer-role { margin-top: 6px; font-size: 10.5px; color: var(--ink); }

  .footer-band {
    position: absolute; left: 0; bottom: 26px; width: 100%; height: 74px;
    background: var(--brand-black); color: var(--footer-text);
    font-family: "Saira Extra Condensed", "Arial Narrow", sans-serif;
    font-weight: 500; font-size: 12px; line-height: 16px; letter-spacing: 0.2px;
    white-space: nowrap;
  }
  .footer-stripe {
    position: absolute; left: 0; bottom: 0; width: 100%; height: 18px;
    background: var(--brand-yellow);
  }

  .parent-company { position: absolute; left: 24px; top: 28px; display: flex; align-items: center; gap: 8px; }
  .parent-dot { width: 16px; height: 16px; border-radius: 50%; background: var(--footer-text); flex: none; }
  .parent-name { font-size: 12px; letter-spacing: 0.8px; text-transform: uppercase; color: var(--footer-text); }

  .footer-divider { position: absolute; left: 236px; top: 14px; width: 1px; height: 46px; background: var(--footer-text); }
  .postal-address { position: absolute; left: 248px; top: 13px; font-style: normal; }
  .postal-address .web { color: var(--brand-yellow); }

  .contact-list { position: absolute; left: 414px; top: 13px; list-style: none; }
  .contact-list li { display: flex; align-items: center; gap: 6px; height: 16px; }
  .contact-icon { width: 10px; height: 10px; fill: var(--brand-yellow); flex: none; }
  .social-mark { width: 8px; height: 8px; margin: 0 1px; background: var(--brand-yellow); flex: none; }
</style>
</head>
<body>
  <main class="letterhead">
    <header>
      <div class="header-band"></div>
      <div class="brand-name">TARVON</div>
      <svg class="tagline-ribbon" viewBox="0 0 250 24" aria-hidden="true">
        <polygon points="14,0 250,0 250,24 0,24" fill="#fbee3f"/>
      </svg>
      <div class="tagline-text">PROUDLY KUWAITI &amp; SUPERIOR QUALITY</div>
    </header>

    <section class="letter-body">
      <p>Letterhead samples are a helpful way of deciding what kind of letterhead you want to design for your company. The internet holds plenty of good ideas to browse, from simple layouts with a bold header to refined designs that place your logo and details at the top and bottom of the page.</p>
      <p>Any business can benefit from reviewing a few letterhead samples before deciding on its own. A clear letterhead shows customers that the company is organised and professional, and it becomes one more tool that supports every letter, quote and invoice you send out.</p>
      <p>Whether you want to reach new customers or remind existing clients of your service, a well made letterhead helps. Keep it simple, keep it consistent, and let it work as a quiet part of your networking, marketing and advertising.</p>
    </section>

    <div class="sign-off">
      <div class="signature-area" role="img" aria-label="Handwritten signature of the company director"></div>
      <div class="signer-role">company director</div>
    </div>

    <footer>
      <div class="footer-band">
        <div class="parent-company">
          <span class="parent-dot"></span>
          <span class="parent-name">Kuwait Morel Oils Co.</span>
        </div>
        <div class="footer-divider"></div>
        <address class="postal-address">
          <div>P.O. Boc 4827</div>
          <div>Qurain 73504, Kuwait</div>
          <div class="web">www.tarvonfluids.example</div>
        </address>
        <ul class="contact-list">
          <li>
            <svg class="contact-icon" viewBox="0 0 10 10" aria-hidden="true"><path d="M2 0.5 L3.6 0.5 L4.3 2.8 L3.1 3.7 C3.7 5 4.9 6.2 6.3 6.9 L7.2 5.7 L9.5 6.4 L9.5 8 C9.5 8.9 8.8 9.5 7.9 9.5 C3.9 9.2 0.8 6.1 0.5 2.1 C0.5 1.2 1.1 0.5 2 0.5 Z"/></svg>
            <span>(+965) 24718593</span>
          </li>
          <li>
            <svg class="contact-icon" viewBox="0 0 10 10" aria-hidden="true"><path d="M0.5 2 H9.5 V8.5 H0.5 Z M1.2 2.6 L5 5.4 L8.8 2.6" fill="none" stroke="#fbee3f" stroke-width="1"/></svg>
            <span>info@tarvonfluids.example</span>
          </li>
          <li>
            <span class="social-mark"></span>
            <span>@TarvonFluids</span>
          </li>
        </ul>
      </div>
      <div class="footer-stripe"></div>
    </footer>
  </main>
</body>
</html>
```